Folder Design: Mobile Laboratory Service

Need a folder designed for a Mobile Laboratory Service. Folder needs to be very professional and will be used to hold brochure, contract and business card of business. Logos of the company are attached.

Industry/Entity Type

Healthcare

```html
<!DOCTYPE html>
<html lang="en">
<head>
<meta charset="utf-8">
<title>Corvane Diagnostics — Presentation Folder</title>
<link rel="stylesheet" href="https://fonts.googleapis.com/css2?family=Montserrat:wght@400;500;600&display=swap">
<style>
  :root {
    --backdrop: #3a3b3d;
    --navy: #06112e;
    --navy-mid: #0a1a44;
    --paper: #f4f6fa;
    --paper-shade: #e4e9f1;
    --sky: #2b8de6;
    --sky-light: #5ab4ec;
    --sky-deep: #1673d8;
    --ink-light: #e8f1fb;
  }
  * { margin: 0; padding: 0; box-sizing: border-box; }
  html, body { width: 1200px; height: 1200px; overflow: hidden; }
  body {
    background: var(--backdrop);
    font-family: "Montserrat", sans-serif;
    display: flex;
    flex-direction: column;
    align-items: center;
    justify-content: center;
    gap: 44px;
  }
  .spread {
    display: flex;
    width: 820px;
    height: 546px;
    box-shadow: 0 18px 40px rgba(0,0,0,.45);
  }
  .panel { position: relative; width: 410px; height: 546px; overflow: hidden; }

  /* outside: back cover */
  .back-cover { background: linear-gradient(160deg, #ffffff, var(--paper-shade)); }
  .back-cover .wave { position: absolute; left: 0; bottom: 0; width: 410px; height: 200px; }
  .brand {
    position: absolute; left: 0; right: 0; top: 120px;
    display: flex; flex-direction: column; align-items: center; gap: 18px;
  }
  .brand-dot { width: 92px; height: 92px; border-radius: 50%; border: 6px solid var(--sky); }
  .brand-name {
    font-weight: 500; font-size: 15px; letter-spacing: .16em;
    text-transform: uppercase; color: var(--sky); text-align: center; line-height: 1.6;
  }
  .contact {
    position: absolute; left: 40px; right: 30px; bottom: 26px;
    display: flex; justify-content: space-between;
    color: var(--ink-light); font-size: 10px; line-height: 1.55;
  }
  .contact-col { display: flex; flex-direction: column; gap: 2px; }
  .contact-line { display: flex; align-items: flex-start; gap: 6px; }
  .contact-line svg { flex: none; width: 10px; height: 10px; margin-top: 2px; }

  /* outside: front cover */
  .front-cover { background: radial-gradient(ellipse at 70% 20%, var(--navy-mid), var(--navy) 70%); }
  .front-cover .brand { top: 110px; }

  /* inside */
  .inside-left { background: linear-gradient(150deg, #ffffff, var(--paper-shade)); border-right: 1px solid #d3d9e2; }
  .inside-right { background: linear-gradient(150deg, #ffffff, #eef1f6); }
  .pocket {
    position: absolute; left: 0; right: 0; bottom: 0; height: 190px;
    background: linear-gradient(120deg, var(--sky-deep), var(--sky-light) 55%, var(--sky-deep));
    border-top-left-radius: 34px;
  }
  .card-slot { position: absolute; width: 2px; height: 44px; background: rgba(10,40,90,.35); transform: rotate(-40deg); }
  .card-slot.first { left: 150px; top: 110px; }
  .card-slot.second { left: 330px; top: 40px; }
</style>
</head>
<body>

<section class="spread outside">
  <div class="panel back-cover">
    <div class="brand">
      <div class="brand-dot"></div>
      <div class="brand-name">Corvane<br>Diagnostics</div>
    </div>
    <svg class="wave" viewBox="0 0 410 200" preserveAspectRatio="none">
      <defs>
        <linearGradient id="waveBlue" x1="0" x2="1">
          <stop offset="0" stop-color="#1a7ee6"/>
          <stop offset="0.6" stop-color="#7cc4f4"/>
          <stop offset="1" stop-color="#1a7ee6"/>
        </linearGradient>
      </defs>
      <path d="M0 58 C120 40 240 90 410 18 L410 200 L0 200 Z" fill="url(#waveBlue)"/>
      <path d="M0 66 C120 52 240 102 410 28 L410 200 L0 200 Z" fill="#ffffff"/>
      <path d="M0 72 C120 60 240 110 410 36 L410 200 L0 200 Z" fill="#06112e"/>
    </svg>
    <div class="contact">
      <div class="contact-col">
        <div class="contact-line">
          <svg viewBox="0 0 10 10"><path d="M2 1 L4 3 L3 4 Q4 6 6 7 L7 6 L9 8 L8 9.5 Q3 9 .5 2 Z" fill="#2b8de6"/></svg>
          <span>(000) 000 0000</span>
        </div>
        <div class="contact-line">
          <svg viewBox="0 0 10 10"><rect x=".5" y="2" width="9" height="6.5" fill="none" stroke="#2b8de6"/><path d="M.5 2 L5 6 L9.5 2" fill="none" stroke="#2b8de6"/></svg>
          <span>email@company.com</span>
        </div>
      </div>
      <div class="contact-col">
        <div class="contact-line">
          <svg viewBox="0 0 10 10"><circle cx="5" cy="5" r="4.3" fill="none" stroke="#2b8de6"/><path d="M.7 5 H9.3 M5 .7 Q2 5 5 9.3 Q8 5 5 .7" fill="none" stroke="#2b8de6"/></svg>
          <span>www.company.com</span>
        </div>
        <div class="contact-line">
          <svg viewBox="0 0 10 10"><path d="M5 9.6 Q1.2 5.5 1.2 3.8 A3.8 3.8 0 0 1 8.8 3.8 Q8.8 5.5 5 9.6 Z" fill="none" stroke="#2b8de6"/><circle cx="5" cy="3.8" r="1.3" fill="#2b8de6"/></svg>
          <span>123 Name Street, 000<br>Your City, 00000-000</span>
        </div>
      </div>
    </div>
  </div>

  <div class="panel front-cover">
    <div class="brand">
      <div class="brand-dot"></div>
      <div class="brand-name">Corvane<br>Diagnostics</div>
    </div>
  </div>
</section>

<section class="spread inside">
  <div class="panel inside-left"></div>
  <div class="panel inside-right">
    <div class="pocket">
      <span class="card-slot first"></span>
      <span class="card-slot second"></span>
    </div>
  </div>
</section>

</body>
</html>
```